Kestrel Roadway Wheels

I need a wrap designed for a box truck. The company is a mobile tire shop. It’s a tire shop on wheels, that comes anywhere you are to service your tires.

```html
<!DOCTYPE html>
<html lang="en">
<head>
<meta charset="utf-8">
<title>Kestrel Roadway Wheels – Box Truck Wrap</title>
<link href="https://fonts.googleapis.com/css2?family=Oswald:wght@400;500&family=Exo+2:ital,wght@1,800;1,900&display=swap" rel="stylesheet">
<style>
  :root {
    --page: #e4e4e4;
    --panel: #141414;
    --panel-deep: #0a0a0a;
    --blue: #1ea3e6;
    --white: #ffffff;
    --strip: #ffffff;
    --badge-grey: #c9c9c9;
  }
  html, body { margin: 0; padding: 0; }
  body {
    width: 1200px; height: 1200px; overflow: hidden;
    background: var(--page);
    position: relative;
  }
  .wrap-panel {
    position: absolute; left: 40px; top: 387px;
    width: 1120px; height: 426px;
    background: radial-gradient(ellipse at 70% 40%, #1f1f1f 0%, var(--panel) 45%, var(--panel-deep) 100%);
    overflow: hidden;
    box-shadow: 0 6px 14px rgba(0,0,0,.35);
  }
  .panel-shapes { position: absolute; inset: 0; }
  .tire-photo {
    position: absolute; left: 358px; top: 139px; width: 440px; height: 236px;
    background: radial-gradient(ellipse at 55% 45%, #6a6a6a 0%, #3a3a3a 45%, rgba(20,20,20,0) 75%);
  }
  .headline-top, .headline-band {
    position: absolute; left: 23px; margin: 0;
    font-family: "Oswald", sans-serif; font-weight: 400;
    font-size: 31px; line-height: 1; color: var(--white);
    letter-spacing: 0.2px; transform: scaleX(0.86); transform-origin: left center;
  }
  .headline-top { top: 28px; }
  .headline-band { top: 75px; }
  .brand-name {
    position: absolute; left: 24px; top: 134px; margin: 0;
    font-family: "Oswald", sans-serif; font-weight: 500;
    font-size: 74px; line-height: 1; letter-spacing: 1px;
    color: var(--white);
  }
  .brand-sub {
    position: absolute; left: 26px; top: 232px; margin: 0;
    font-family: "Exo 2", sans-serif; font-style: italic; font-weight: 900;
    font-size: 36px; line-height: 1; color: var(--white);
  }
  .phone {
    position: absolute; left: 24px; top: 300px; height: 68px;
    display: flex; align-items: center; gap: 10px;
    font-family: "Oswald", sans-serif; font-weight: 500;
    font-size: 50px; color: var(--white); line-height: 1;
  }
  .phone span { display: inline-block; transform: scaleX(0.88); transform-origin: left center; white-space: nowrap; }
  .phone svg { width: 36px; height: 36px; flex: none; }
  .company-mark {
    position: absolute; left: 586px; top: 36px;
    display: flex; align-items: center; gap: 10px;
  }
  .company-mark .dot { width: 22px; height: 22px; border-radius: 50%; background: var(--blue); flex: none; }
  .company-mark .name {
    font-family: "Oswald", sans-serif; font-weight: 500;
    font-size: 27px; line-height: 1.08; color: var(--white); margin: 0;
  }
  .services {
    position: absolute; right: 26px; top: 22px; margin: 0; padding: 0; list-style: none;
  }
  .services li {
    display: flex; align-items: center; justify-content: flex-end; gap: 14px;
    height: 36.6px;
    font-family: "Oswald", sans-serif; font-weight: 400; font-size: 22px;
    color: var(--white);
  }
  .services li span { transform: scaleX(0.86); transform-origin: right center; display: inline-block; white-space: nowrap; }
  .services svg { width: 30px; height: 30px; flex: none; }
  .quote-line {
    position: absolute; right: 26px; margin: 0; text-align: right;
    font-family: "Exo 2", sans-serif; font-style: italic; font-weight: 900; line-height: 1;
  }
  .quote-top { top: 270px; font-size: 26px; color: var(--white); }
  .quote-main {
    top: 296px; font-size: 44px; color: var(--blue);
    -webkit-text-stroke: 1.5px var(--white);
  }
  .partner-strip {
    position: absolute; left: 0; bottom: 0; width: 100%; height: 54px;
    display: flex; align-items: center; justify-content: flex-end; gap: 18px;
    padding-right: 28px; box-sizing: border-box;
  }
  .partner-badge { height: 16px; background: var(--badge-grey); border-radius: 2px; }
</style>
</head>
<body>
  <section class="wrap-panel" aria-label="Box truck side wrap">
    <svg class="panel-shapes" viewBox="0 0 1120 426" width="1120" height="426" aria-hidden="true">
      <defs>
        <linearGradient id="swoosh" x1="0" y1="0" x2="1" y2="0">
          <stop offset="0" stop-color="#3c3c3c"/>
          <stop offset="0.5" stop-color="#d8d8d8"/>
          <stop offset="1" stop-color="#555"/>
        </linearGradient>
      </defs>
      <path d="M455 0 H590 C650 20 670 80 668 140 L640 140 C640 90 610 40 540 22 C510 14 480 8 455 0 Z" fill="url(#swoosh)"/>
      <rect x="0" y="68" width="513" height="47" fill="var(--blue)"/>
      <polygon points="0,296 353,296 323,371 0,371" fill="var(--blue)"/>
      <path d="M288 426 C310 395 330 378 355 373 H1120 V426 Z" fill="var(--strip)"/>
      <path d="M300 426 C320 398 338 382 365 375 L340 375 C318 382 300 402 288 426 Z" fill="#9a9a9a"/>
    </svg>

    <div class="tire-photo" role="img" aria-label="Photo of a stack of off-road tires with deep tread"></div>

    <p class="headline-top">THIS TRUCK CARRIES ALL THE EQUIPMENT</p>
    <p class="headline-band">NEEDED TO GET YOUR BACK ON THE ROAD!</p>

    <h1 class="brand-name">KESTREL WHEELS</h1>
    <p class="brand-sub">MOBILE TIRES</p>

    <div class="phone">
      <svg viewBox="0 0 24 24" aria-hidden="true"><path fill="#fff" d="M6.6 10.8a15.1 15.1 0 0 0 6.6 6.6l2.2-2.2a1 1 0 0 1 1-.25 11.4 11.4 0 0 0 3.6.57 1 1 0 0 1 1 1V20a1 1 0 0 1-1 1A17 17 0 0 1 3 4a1 1 0 0 1 1-1h3.5a1 1 0 0 1 1 1c0 1.25.2 2.45.57 3.57a1 1 0 0 1-.25 1z"/></svg>
      <span>555-010-4477</span>
    </div>

    <div class="company-mark">
      <span class="dot"></span>
      <p class="name">Kestrel Roadway<br>Wheels</p>
    </div>

    <ul class="services">
      <li><span>EMERGENCY ROADSIDE SERVICE</span><svg viewBox="0 0 30 30" aria-hidden="true"><circle cx="15" cy="15" r="13" fill="none" stroke="#1ea3e6" stroke-width="2"/><circle cx="15" cy="15" r="9" fill="#1ea3e6"/></svg></li>
      <li><span>NEW &amp; USED TIRES</span><svg viewBox="0 0 30 30" aria-hidden="true"><circle cx="15" cy="15" r="13" fill="none" stroke="#1ea3e6" stroke-width="2"/><circle cx="15" cy="15" r="9" fill="#1ea3e6"/></svg></li>
      <li><span>COMPETITIVE&nbsp; WHOLESALE PRICING</span><svg viewBox="0 0 30 30" aria-hidden="true"><circle cx="15" cy="15" r="13" fill="none" stroke="#1ea3e6" stroke-width="2"/><circle cx="15" cy="15" r="9" fill="#1ea3e6"/></svg></li>
      <li><span>TIRE REPAIRS</span><svg viewBox="0 0 30 30" aria-hidden="true"><circle cx="15" cy="15" r="13" fill="none" stroke="#1ea3e6" stroke-width="2"/><circle cx="15" cy="15" r="9" fill="#1ea3e6"/></svg></li>
      <li><span>TIRE MOUNTING &amp; INSTALLATION</span><svg viewBox="0 0 30 30" aria-hidden="true"><circle cx="15" cy="15" r="13" fill="none" stroke="#1ea3e6" stroke-width="2"/><circle cx="15" cy="15" r="9" fill="#1ea3e6"/></svg></li>
      <li><span>LOW PROFILE TIRES &amp; CUSTOM WHEELS</span><svg viewBox="0 0 30 30" aria-hidden="true"><circle cx="15" cy="15" r="13" fill="none" stroke="#1ea3e6" stroke-width="2"/><circle cx="15" cy="15" r="9" fill="#1ea3e6"/></svg></li>
    </ul>

    <p class="quote-line quote-top">“DON’T WAIT AT A TIRE SHOP,</p>
    <p class="quote-line quote-main">WHEEL COME TO YOU!”</p>

    <div class="partner-strip" aria-label="Tire brands carried">
      <span class="partner-badge" style="width:80px"></span>
      <span class="partner-badge" style="width:58px"></span>
      <span class="partner-badge" style="width:90px"></span>
      <span class="partner-badge" style="width:92px"></span>
      <span class="partner-badge" style="width:84px"></span>
      <span class="partner-badge" style="width:58px"></span>
      <span class="partner-badge" style="width:92px"></span>
      <span class="partner-badge" style="width:92px"></span>
    </div>
  </section>
</body>
</html>
```